Website for software company "velbra"

We need a website for our software company/startup named "velbra". We are developing several products (currently 3 standard-software products) which are all in different sectors, but all our products are available for Laptops/PC/Mobile Phones/Tablets, ... We do also create custom software and support our customers with consulting to optimize their processes.
We already have a Logo which you can find in the attached files.
We are a young team of 4 members (two founders and 2 employees).

To get an idea of our products -> the first one is a planning software for healthcare organizations (eg. Mercyway, firebrigade, pharmacy), the second one is a booking software for sport clubs and the third one is a competition software for sports hunting. You see very diverse. Include or ignore this info of our products as you like.

The design has to be a bootstrap 4 (or higher) design. We have licenced FontAwesome as iconset. Responsive design should come without saying.

Coding

Coded - Design and coding required

Number of Pages Required

5+ page

Font styles to use
Sans Serif

Requirements
Must have
• Starting page, product pages, news section, contact, team, services

```html
<!DOCTYPE html>
<html lang="en">
<head>
<meta charset="utf-8">
<title>velbra – Software that optimizes processes</title>
<link href="https://fonts.googleapis.com/css2?family=Montserrat:wght@300;400;500;600;700;800&display=swap" rel="stylesheet">
<style>
:root{
  --orange:#f47b20;
  --orange-soft:#f9a15d;
  --ink:#1f2633;
  --navy:#141c2b;
  --text:#3a3f4a;
  --muted:#7a808c;
  --light:#f3f4f6;
  --line:#e2e4e8;
  --white:#ffffff;
}
*{box-sizing:border-box;margin:0;padding:0}
html,body{width:1200px;height:5200px;overflow:hidden}
body{font-family:'Montserrat',Arial,sans-serif;color:var(--text);background:var(--white)}
section,header,footer{position:relative;width:1200px;overflow:hidden}
.btn{display:inline-block;background:var(--orange);color:var(--white);font-weight:700;font-size:15px;letter-spacing:.5px;padding:14px 30px;border-radius:30px;text-transform:uppercase}
.btn-outline{display:inline-block;border:2px solid var(--orange);color:var(--orange);font-weight:700;font-size:12px;padding:7px 20px;border-radius:20px;text-transform:uppercase}
.btn-dark{background:var(--ink)}
.placeholder{border-radius:8px}
p{font-size:15px;line-height:1.6}

/* header + hero */
.hero{height:760px;background:linear-gradient(180deg,#fafafa,#ffffff)}
.nav{position:absolute;top:0;left:0;width:1200px;height:100px;display:flex;align-items:center;padding:0 120px}
.brand{font-size:40px;font-weight:800;color:var(--ink);letter-spacing:1px;display:flex;align-items:center;gap:10px}
.brand-dot{width:16px;height:16px;background:var(--orange);border-radius:50%}
.nav ul{list-style:none;display:flex;gap:46px;margin-left:auto;align-items:center;font-size:13px;font-weight:600;color:var(--ink)}
.nav li.active{color:var(--orange);border-bottom:2px solid var(--orange);padding-bottom:6px}
.nav .btn{font-size:13px;padding:10px 24px}
.hero-copy{position:absolute;left:120px;top:220px;width:520px}
.hero-copy h1{font-size:44px;line-height:1.12;color:var(--ink);font-weight:800;text-transform:uppercase}
.hero-copy h1 span{font-weight:400;display:block}
.hero-copy p{margin:18px 0 28px;width:400px;color:var(--muted)}
.hero-art{position:absolute;left:650px;top:120px;width:470px;height:520px;border-radius:50%;background:radial-gradient(circle at 50% 50%,#fde3cc 0%,#fbefe4 45%,#f7f7f8 70%)}
.hero-wave{position:absolute;left:0;bottom:0}

/* welcome */
.welcome{height:410px;text-align:center;padding-top:40px}
.section-title{font-size:34px;font-weight:400;color:var(--ink);text-transform:uppercase;letter-spacing:1px}
.section-title b{font-weight:800;color:var(--orange)}
.section-title.dark b{color:var(--ink)}
.welcome p{width:800px;margin:30px auto 30px;color:var(--muted)}

/* products */
.products{height:610px;background:radial-gradient(ellipse at 70% 60%,#243349,#0f1624 75%);color:var(--white)}
.products .section-title{position:absolute;top:40px;width:1200px;text-align:center;color:var(--white)}
.products .section-title b{color:var(--orange)}
.product-copy{position:absolute;width:400px}
.product-copy h2{font-size:30px;font-weight:800;color:var(--orange);text-transform:uppercase;margin-bottom:16px}
.product-copy h2 span{color:var(--ink)}
.products .product-copy h2 span{color:var(--white)}
.product-copy p{margin-bottom:14px;color:var(--muted)}
.products .product-copy p{color:#c3c8d2}
.product-copy .btn{margin-top:10px}

.booking{height:580px}
.booking-accent{position:absolute;left:0;top:50px;width:360px;height:400px;background:var(--orange);border-radius:0 24px 24px 0}
.competition{height:500px}

/* services */
.services{height:560px;background:var(--light)}
.services .section-title{position:absolute;left:630px;top:90px;text-align:left}
.service-list{position:absolute;left:630px;top:160px;list-style:none}
.service-list li{display:flex;align-items:center;gap:24px;margin-bottom:34px}
.service-icon{width:80px;height:80px;border-radius:50%;background:var(--ink);border:4px solid #c9ccd2;display:flex;align-items:center;justify-content:center;flex:none}
.service-list h3{font-size:14px;font-weight:800;color:var(--ink);text-transform:uppercase;margin-bottom:6px}
.service-list p{font-size:12px;width:360px;color:var(--muted);line-height:1.5}

/* team */
.team{height:540px;text-align:center;padding-top:60px}
.team-grid{display:flex;justify-content:center;gap:22px;margin-top:50px}
.member{width:234px;height:280px;border:1px solid var(--line);padding:10px;box-shadow:0 4px 12px rgba(0,0,0,.06)}
.member .placeholder{height:185px;border-radius:0}
.member h4{font-size:15px;font-weight:800;color:var(--ink);text-transform:uppercase;margin-top:18px}
.member span{font-size:13px;color:var(--muted)}

/* news */
.news{height:540px;background:var(--light)}
.news .section-title{position:absolute;left:140px;top:50px}
.news-grid{position:absolute;left:140px;top:130px;display:flex;gap:28px}
.news-card{width:290px;height:360px;background:var(--white);box-shadow:0 6px 16px rgba(0,0,0,.08)}
.news-card .placeholder{height:165px;border-radius:0}
.news-body{padding:16px 20px}
.news-body time{font-size:11px;font-weight:700;color:var(--ink)}
.news-body h4{font-size:13px;font-weight:700;color:var(--ink);margin:6px 0 8px;line-height:1.35}
.news-body p{font-size:11px;color:var(--muted);line-height:1.5;margin-bottom:12px}

/* cta */
.cta{height:320px;background:linear-gradient(90deg,#f26f13,#f7913e);text-align:center;color:var(--white);padding-top:50px}
.cta-mark{font-size:26px;font-weight:800;letter-spacing:1px}
.cta h2{font-size:32px;font-weight:800;text-transform:uppercase;line-height:1.2;margin:16px 0 28px}
.cta h2 span{font-weight:400;display:block}

/* footer */
.site-footer{height:380px;background:var(--ink);color:#b9bec8;padding:60px 170px 0;display:flex;gap:60px}
.footer-brand{width:280px}
.footer-brand .brand{color:var(--white);font-size:40px}
.footer-brand p{font-size:11px;margin:16px 0;color:#8e94a0}
.footer-brand small{font-size:11px;color:var(--white)}
.footer-col{border-left:1px solid #3a4252;padding-left:18px;width:170px}
.footer-col h5{font-size:12px;color:var(--orange);text-transform:uppercase;margin-bottom:14px;font-weight:700}
.footer-col ul{list-style:none;font-size:12px;line-height:2}
.socials{display:flex;gap:8px}
.socials span{width:26px;height:26px;border-radius:50%;background:var(--orange)}
</style>
</head>
<body>

<header class="hero">
  <nav class="nav">
    <div class="brand"><span class="brand-dot"></span>velbra</div>
    <ul>
      <li class="active">Product</li>
      <li>Services</li>
      <li>News</li>
      <li>Team</li>
      <li>About</li>
      <li><span class="btn">Contact</span></li>
    </ul>
  </nav>
  <div class="hero-copy">
    <h1><span>We help customer</span>to optimize their processes</h1>
    <p>Lorem ipsum dolor sit amet, consectetur adipiscing elit, sed do eiusmod tempor incididunt.</p>
    <span class="btn">Learn more</span>
  </div>
  <div class="hero-art" role="img" aria-label="Large brand emblem surrounded by orbit rings with optimize and support badges"></div>
  <svg class="hero-wave" width="1200" height="160" viewBox="0 0 1200 160">
    <path d="M0 20 C300 150 800 170 1200 40 L1200 160 L0 160 Z" fill="#ffffff"/>
    <path d="M0 20 C300 150 800 170 1200 40" fill="none" stroke="#f47b20" stroke-width="10"/>
  </svg>
</header>

<section class="welcome">
  <h2 class="section-title dark">Welcome to <b style="color:var(--orange)">velbra</b></h2>
  <p>Lorem ipsum dolor sit amet, consectetur adipiscing elit, sed do eiusmod tempor incididunt ut labore et dolore magna aliqua. Ut enim ad minim veniam, quis nostrud exercitation ullamco laboris nisi ut aliquip ex ea commodo consequat. Duis aute irure dolor in.</p>
  <span class="btn">Learn more</span>
</section>

<section class="products">
  <h2 class="section-title">Our <b>Products</b></h2>
  <div class="product-copy" style="left:130px;top:190px">
    <h2>Planning <span>Software</span></h2>
    <p>Lorem ipsum dolor sit amet, consectetur adipiscing elit, sed do eiusmod tempor incididunt ut labore et dolore magna aliqua. Ut enim ad minim veniam, quis nostrud.</p>
    <p>exercitation ullamco laboris nisi ut aliquip ex ea commodo consequat. Duis aute irure dolor.</p>
    <span class="btn">Learn more</span>
  </div>
  <div class="placeholder" role="img" aria-label="Laptop showing the planning software dashboard" style="position:absolute;left:690px;top:130px;width:500px;height:360px;background:linear-gradient(160deg,#e9eef6,#b9c6d8)"></div>
</section>

<section class="booking">
  <div class="booking-accent"></div>
  <div class="placeholder" role="img" aria-label="Tablet and phone showing the booking software" style="position:absolute;left:100px;top:80px;width:420px;height:380px;background:linear-gradient(160deg,#ffffff,#dfe6f2)"></div>
  <div class="product-copy" style="left:665px;top:110px;width:420px">
    <h2>Booking <span>Software</span></h2>
    <p>Lorem ipsum dolor sit amet, consectetur adipiscing elit, sed do eiusmod tempor incididunt ut labore et dolore magna aliqua. Ut enim ad minim veniam, quis nostrud.</p>
    <p>exercitation ullamco laboris nisi ut aliquip ex ea commodo consequat. Duis aute irure dolor.</p>
    <span class="btn">Learn more</span>
  </div>
</section>

<section class="competition">
  <div class="product-copy" style="left:125px;top:100px;width:420px">
    <h2>Competition <span>Software</span></h2>
    <p>Lorem ipsum dolor sit amet, consectetur adipiscing elit, sed do eiusmod tempor incididunt ut labore et dolore magna aliqua. Ut enim ad minim veniam, quis nostrud.</p>
    <p>exercitation ullamco laboris nisi ut aliquip ex ea commodo consequat. Duis aute irure dolor.</p>
    <span class="btn">Learn more</span>
  </div>
  <div class="placeholder" role="img" aria-label="Laptop showing the competition software results" style="position:absolute;left:570px;top:80px;width:520px;height:320px;background:linear-gradient(160deg,#eef2f8,#c3cddb)"></div>
</section>

<section class="services">
  <div class="placeholder" role="img" aria-label="Isometric illustration of devices and a team at work" style="position:absolute;left:60px;top:90px;width:500px;height:380px;background:linear-gradient(160deg,#f7f7f8,#dcdfe4)"></div>
  <h2 class="section-title dark">velbra <b>Services</b></h2>
  <ul class="service-list">
    <li><span class="service-icon"><svg width="34" height="24" viewBox="0 0 34 24" fill="none" stroke="#fff" stroke-width="3"><path d="M10 3 2 12l8 9M24 3l8 9-8 9"/></svg></span>
      <div><h3>Custom Software</h3><p>Lorem ipsum dolor sit amet, consectetur adipiscing elit, sed do eiusmod tempor incididunt ut labore.</p></div></li>
    <li><span class="service-icon" style="background:var(--orange)"><svg width="32" height="30" viewBox="0 0 32 30" fill="none" stroke="#fff" stroke-width="3"><path d="M4 18v-4a12 12 0 0 1 24 0v4"/><rect x="2" y="17" width="6" height="9" rx="2"/><rect x="24" y="17" width="6" height="9" rx="2"/></svg></span>
      <div><h3>Customer Support</h3><p>Lorem ipsum dolor sit amet, consectetur adipiscing elit, sed do eiusmod tempor incididunt ut labore.</p></div></li>
    <li><span class="service-icon"><svg width="30" height="30" viewBox="0 0 30 30" fill="none" stroke="#fff" stroke-width="3"><circle cx="15" cy="15" r="6"/><path d="M15 2v5M15 23v5M2 15h5M23 15h5M6 6l3 3M21 21l3 3M6 24l3-3M21 9l3-3"/></svg></span>
      <div><h3>Optimize Process</h3><p>Lorem ipsum dolor sit amet, consectetur adipiscing elit, sed do eiusmod tempor incididunt ut labore.</p></div></li>
  </ul>
</section>

<section class="team">
  <h2 class="section-title dark">Meet <b>Our Team</b></h2>
  <div class="team-grid">
    <div class="member"><div class="placeholder" role="img" aria-label="Portrait photo of co-founder" style="background:linear-gradient(180deg,#e9ebee,#c8ccd3)"></div><h4>Alden Marsh</h4><span>Co Founder</span></div>
    <div class="member"><div class="placeholder" role="img" aria-label="Portrait photo of partner" style="background:linear-gradient(180deg,#eceef0,#cfd3d8)"></div><h4>Priya K.</h4><span>Partners</span></div>
    <div class="member"><div class="placeholder" role="img" aria-label="Portrait photo of developer" style="background:linear-gradient(180deg,#e8eaed,#c5c9d0)"></div><h4>Tomas R.</h4><span>Developer</span></div>
    <div class="member"><div class="placeholder" role="img" aria-label="Portrait photo of marketing lead" style="background:linear-gradient(180deg,#eceef0,#d0d3d8)"></div><h4>Elena V.</h4><span>Marketing</span></div>
  </div>
</section>

<section class="news">
  <h2 class="section-title dark">Latest <b>News</b></h2>
  <div class="news-grid">
    <article class="news-card"><div class="placeholder" role="img" aria-label="Photo of hands typing on a laptop" style="background:linear-gradient(160deg,#6b7482,#2e3542)"></div>
      <div class="news-body"><time>JUN 14, 2022</time><h4>Sed ut perspiciatis unde omnis iste natus error sit voluptatem</h4><p>Lorem ipsum dolor sit amet, consectetur adipiscing elit sed do.</p><span class="btn-outline">Learn more</span></div></article>
    <article class="news-card"><div class="placeholder" role="img" aria-label="Photo of a team meeting at a desk" style="background:linear-gradient(160deg,#d9d6d2,#9a9690)"></div>
      <div class="news-body"><time>JUN 09, 2022</time><h4>Sed ut perspiciatis unde omnis iste natus error sit voluptatem</h4><p>Lorem ipsum dolor sit amet, consectetur adipiscing elit sed do.</p><span class="btn-outline">Learn more</span></div></article>
    <article class="news-card"><div class="placeholder" role="img" aria-label="Photo of code on a monitor in warm light" style="background:linear-gradient(160deg,#c0703a,#3a2a22)"></div>
      <div class="news-body"><time>JUN 02, 2022</time><h4>Sed ut perspiciatis unde omnis iste natus error sit voluptatem</h4><p>Lorem ipsum dolor sit amet, consectetur adipiscing elit sed do.</p><span class="btn-outline">Learn more</span></div></article>
  </div>
</section>

<section class="cta">
  <div class="cta-mark">velbra</div>
  <h2>Sed ut perspiciatis unde omnis iste<span>natus error sit voluptatem</span></h2>
  <span class="btn btn-dark">Contact us</span>
</section>

<footer class="site-footer">
  <div class="footer-brand">
    <div class="brand"><span class="brand-dot"></span>velbra</div>
    <p>Lorem ipsum dolor sit amet, consectetur adipiscing elit, sed do eiusmod tempor incididunt ut labore.</p>
    <small>© 2022 velbra · All Rights Reserved</small>
  </div>
  <div class="footer-col"><h5>Navigation</h5><ul><li>About Us</li><li>Products</li><li>Services</li><li>Contact Us</li></ul></div>
  <div class="footer-col"><h5>Resources</h5><ul><li>News</li><li>Team</li><li>Privacy Policy</li></ul></div>
  <div class="footer-col"><h5>Follow Us</h5><div class="socials"><span></span><span></span><span></span><span></span></div></div>
</footer>

</body>
</html>
```